Real Estate Seller Financing Postcard

I need a postcard that lays out these options contained in the notes that grabs attention, explains the two options easily and is eye-catching. The front needs to have the percentages on it and information about it and on the other side One side exact Text is:
"Monthly income without tenant headaches" in big letters. Also on front "Get
110%
add an "or"
160% of market value for your property. ". The percentages should be displayed and that is not to be a sentence of text. Other side text: I need bullets points for these "Formal protection as a lien holder against home
No commission or closing cost
Fast closings possible
Property taken as is so no repairs.

Add to the top of the back in "It’s simple. I am a new investor without down payment capital who still want to double our portfolio this year to grow our portfolio."
Here are the two options that are to be the largest part of the back
Option 1, you can receive 80% now cash and 30% over a short period of time including interest.

Option 2, where act like a bank allowing you to make 150% if you finance the whole property(ies). No gimmicks and surprises, just simple unconventional financing.

Include Logo Somewhere

Target Market(s)

Property Owners Wanting to Sell Their Property

Industry/Entity Type

Real Estate Investing

Requirements
Must have
• The options promiment and each side with its respective information. Must have logo somewhere
Nice to have
• The options in color other than black.
Should not have
• A picture of money on the front. Any other image is okay.

```html
<!DOCTYPE html>
<html lang="en">
<head>
<meta charset="utf-8">
<title>Meridian Real Estate Group Postcard</title>
<link href="https://fonts.googleapis.com/css2?family=Montserrat:wght@300;400;500;600;700;800&display=swap" rel="stylesheet">
<style>
  :root {
    --page-bg: #b9d3ed;
    --card-bg: #ffffff;
    --brand-navy: #1a4590;
    --brand-blue: #1c4fa0;
    --roof-light: #0a72b5;
    --roof-mid: #07569b;
    --chevron-gray: #6d6d6d;
    --ink: #1a1a1a;
    --white: #ffffff;
  }
  * { margin: 0; padding: 0; box-sizing: border-box; }
  html, body { width: 877px; height: 1200px; overflow: hidden; }
  body {
    background: var(--page-bg);
    font-family: "Montserrat", Arial, sans-serif;
    position: relative;
  }
  .postcard {
    position: absolute;
    left: 126px;
    width: 624px;
    height: 448px;
    background: var(--card-bg);
    overflow: hidden;
    box-shadow: 0 2px 6px rgba(40, 60, 90, 0.35);
  }
  .postcard--front { top: 117px; }
  .postcard--back { top: 620px; height: 446px; }
  .card-art { position: absolute; inset: 0; width: 100%; height: 100%; }

  /* Brand lockup */
  .brand {
    position: absolute;
    display: flex;
    align-items: center;
    gap: 10px;
  }
  .brand__dot {
    border: 2px solid var(--brand-blue);
    border-radius: 50%;
    flex: none;
  }
  .brand__rule { width: 1px; background: #777; flex: none; }
  .brand__name { line-height: 1; color: var(--brand-blue); font-weight: 400; }
  .brand__name span { display: block; }
  .brand__title { letter-spacing: 1px; }
  .brand__tag { margin-top: 4px; }

  .postcard--front .brand { left: 176px; top: 28px; }
  .postcard--front .brand__dot { width: 80px; height: 80px; }
  .postcard--front .brand__rule { height: 58px; }
  .postcard--front .brand__title { font-size: 36px; }
  .postcard--front .brand__tag { font-size: 14.5px; color: #555; }

  .postcard--back .brand { left: 218px; top: 372px; }
  .postcard--back .brand__dot { width: 54px; height: 54px; border-color: var(--white); }
  .postcard--back .brand__rule { height: 38px; background: var(--white); }
  .postcard--back .brand__name { color: var(--white); }
  .postcard--back .brand__title { font-size: 26px; }
  .postcard--back .brand__tag { font-size: 11px; margin-top: 2px; }

  /* Front headline */
  .headline {
    position: absolute;
    left: 0; right: 0;
    top: 258px;
    text-align: center;
    color: var(--white);
    line-height: 37px;
    font-size: 30px;
  }
  .headline__light { font-weight: 400; display: block; }
  .headline__bold { font-weight: 800; display: block; letter-spacing: 0.5px; }
  .offer-rule {
    position: absolute;
    left: 121px; width: 381px; top: 376px;
    height: 1px;
    background: rgba(255, 255, 255, 0.45);
  }
  .offer {
    position: absolute;
    left: 0; right: 0; top: 372px;
    text-align: center;
    color: var(--white);
  }
  .offer__figures { font-size: 32px; font-weight: 800; letter-spacing: 1px; line-height: 38px; }
  .offer__note { font-size: 15px; font-weight: 400; line-height: 16px; }

  /* Back copy */
  .intro, .option {
    position: absolute;
    left: 20px;
    color: var(--ink);
  }
  .intro { top: 20px; width: 320px; font-size: 14px; line-height: 16.7px; font-weight: 500; }
  .option--cash { top: 90px; width: 300px; font-size: 14px; line-height: 16.7px; font-weight: 500; }
  .option--finance {
    top: 162px; width: 300px;
    font-size: 11.4px; line-height: 16.3px; text-align: justify;
  }
  .benefits {
    position: absolute;
    left: 38px; top: 226px;
    list-style: none;
    font-size: 10px;
    font-weight: 500;
    color: var(--ink);
  }
  .benefits li { position: relative; padding-left: 14px; height: 23px; line-height: 14px; }
  .benefits li::before {
    content: "";
    position: absolute;
    left: 0; top: 4px;
    width: 5px; height: 5px;
    border-radius: 50%;
    background: var(--ink);
  }

  .stamp-box {
    position: absolute;
    left: 523px; top: 23px;
    width: 79px; height: 79px;
    border: 1px solid var(--ink);
  }
  .address-line {
    position: absolute;
    left: 403px; width: 198px;
    height: 1px;
    background: var(--ink);
  }

  .contact {
    position: absolute;
    left: 32px; top: 411px;
    list-style: none;
    color: var(--white);
    font-size: 8.5px;
  }
  .contact li { display: flex; align-items: center; gap: 8px; height: 13px; }
  .contact svg { width: 11px; height: 11px; }
  .phone {
    position: absolute;
    left: 494px; top: 424px;
    display: flex; align-items: center; gap: 4px;
    color: var(--white);
    font-size: 12px;
    font-weight: 600;
  }
  .phone svg { width: 16px; height: 16px; }
</style>
</head>
<body>

<section class="postcard postcard--front">
  <svg class="card-art" viewBox="0 0 624 448" aria-hidden="true">
    <defs>
      <radialGradient id="roofGlowFront" cx="50%" cy="20%" r="60%">
        <stop offset="0" stop-color="#0877b8"/>
        <stop offset="1" stop-color="#1a4590"/>
      </radialGradient>
    </defs>
    <polygon points="188,224 311,158 434,224 311,175" fill="var(--chevron-gray)"/>
    <polygon points="0,289 311,202 624,289 624,448 0,448" fill="url(#roofGlowFront)"/>
    <polygon points="0,289 311,202 624,289 311,222" fill="var(--roof-light)" opacity="0.55"/>
  </svg>

  <div class="brand">
    <span class="brand__dot"></span>
    <span class="brand__rule"></span>
    <span class="brand__name">
      <span class="brand__title">MERIDIAN</span>
      <span class="brand__tag">REAL ESTATE GROUP</span>
    </span>
  </div>

  <h1 class="headline">
    <span class="headline__light">MONTHLY INCOME</span>
    <span class="headline__bold">WITHOUT TENANT</span>
    <span class="headline__bold">HEADACHES</span>
  </h1>
  <div class="offer-rule"></div>
  <div class="offer">
    <p class="offer__figures">GET 110% OR 160%</p>
    <p class="offer__note">OF MARKET VALUE FOR YOUR PROPERTY.</p>
  </div>
</section>

<section class="postcard postcard--back">
  <svg class="card-art" viewBox="0 0 624 446" aria-hidden="true">
    <defs>
      <radialGradient id="roofGlowBack" cx="50%" cy="35%" r="60%">
        <stop offset="0" stop-color="#0877b8"/>
        <stop offset="1" stop-color="#1a4590"/>
      </radialGradient>
    </defs>
    <polygon points="188,337 311,270 434,337 311,287" fill="var(--chevron-gray)"/>
    <polygon points="0,402 311,315 624,402 624,446 0,446" fill="url(#roofGlowBack)"/>
    <polygon points="0,402 311,315 624,402 311,336" fill="var(--roof-light)" opacity="0.55"/>
  </svg>

  <p class="intro">I am a new investor without down payment capital who still want to double our portfolio this year to grow our portfolio</p>
  <p class="option option--cash">you can receive 80% now cash and 30% over a short period of time including interest.</p>
  <p class="option option--finance">where act like a bank allowing you to make 150% if you finance the whole property(ies). No gimmicks and surprises, just simple unconventional financing.</p>

  <ul class="benefits">
    <li>Formal protection as a lien holder against home</li>
    <li>No commission or closing cost</li>
    <li>Fast closings possible</li>
    <li>Property taken as is so no repairs.</li>
  </ul>

  <div class="stamp-box"></div>
  <div class="address-line" style="top:149px"></div>
  <div class="address-line" style="top:226px"></div>
  <div class="address-line" style="top:301px"></div>

  <div class="brand">
    <span class="brand__dot"></span>
    <span class="brand__rule"></span>
    <span class="brand__name">
      <span class="brand__title">MERIDIAN</span>
      <span class="brand__tag">REAL ESTATE GROUP</span>
    </span>
  </div>

  <ul class="contact">
    <li>
      <svg viewBox="0 0 12 12" fill="none" stroke="#fff" stroke-width="0.9"><circle cx="6" cy="6" r="5"/><ellipse cx="6" cy="6" rx="2.2" ry="5"/><line x1="1" y1="6" x2="11" y2="6"/></svg>
      your website.com
    </li>
    <li>
      <svg viewBox="0 0 12 12" fill="none" stroke="#fff" stroke-width="0.9"><rect x="1" y="2.5" width="10" height="7"/><polyline points="1,2.5 6,7 11,2.5"/></svg>
      mail@meridianmail.com
    </li>
  </ul>

  <div class="phone">
    <svg viewBox="0 0 16 16"><circle cx="8" cy="8" r="8" fill="#fff"/><path d="M5.2 4.2l1.4-.3.8 2-1 .8c.5 1.1 1.3 1.9 2.4 2.4l.8-1 2 .8-.3 1.4c-.2.4-.6.6-1 .5C7.4 10.3 5.7 8.6 4.7 5.2c-.1-.4.1-.8.5-1z" fill="var(--brand-navy)"/></svg>
    (123) 456 789
  </div>
</section>

</body>
</html>
```